Design clean technology service-based company website

Hello, We are looking to reskin our company website. We are an environmental inspection company and test for Asbestos, Lead and Mold along with other contaminants. People depend on the results to be accurate and fast. We are regulated by the EPA and State regulations. We work a lot with business to business and business to customer. We are wanting to make our new presentation to be modern and easy for customers to interact with us, understand our process and services while providing valuable environmental informational resource and updates. We are a technology based company and will be providing instantaneous results as reports come in for the customers. We are needing good calls to action on the site to direct them to setup a new inspection. Each user will have a backend access to their job information with invoices, reports, status, etc. We have developed software to be able to proved these reports and want to look the part.

My current website is www.trypelmarix.com

Helllo we are wanting to make sure we have good time to select the right website for us and also have the additional time to select other pages of the website. We have received great designs and have consolidated our requests into a document for the next set of iterations.

Target Market(s)

Home Owners, Contractors, Engineers, Real Estate Agents, Building Owners, Insurance Adjusters

Industry/Entity Type

Environmental Consultant

Number of Pages Required

5+ page

Font styles to use
Sans Serif

Colors
0355a3
9bcb3c
7f7f7f
f5f5f5
000000

Requirements
Must have
• Use our existing logo to design around
• The layouts look good in mobile mode for understanding and selecting services and signing up
• Clean Modern Layout
• Have all pages on the website have a similar layout and feel
• Clearly communicate services along with bundle service packages
• Detail the customer journey with graphic design
• Great call to actions to either schedule inspection online, call, text, chat
Nice to have
• Have an interactive graphic for where to test for lead, asbestos and mold.
• I like the barney kolts top order line bar - see attached
• Have clear question and answer page layouts for asbestos, lead and mold
• Show Company reviews
• Have clear Resources pages for all types of contaminants
Should not have
• My current website is www.trypelmarix.com

```html
<!DOCTYPE html>
<html lang="en">
<head>
<meta charset="utf-8">
<title>How It Affects Your Health</title>
<link href="https://fonts.googleapis.com/css2?family=Barlow:wght@400;500;600;700&display=swap" rel="stylesheet">
<style>
  :root {
    --frame-dark: #333333;
    --frame-darker: #1f1f1f;
    --page: #ffffff;
    --ink-grey: #6f6f6f;
    --body-grey: #6a6a6a;
    --accent-green: #8dc63f;
    --soft-grey: #f4f4f4;
    --faint-grey: #f5f5f5;
  }
  * { margin: 0; padding: 0; box-sizing: border-box; }
  html, body { width: 1200px; height: 1200px; overflow: hidden; }
  body {
    position: relative;
    background: linear-gradient(160deg, var(--frame-dark) 55%, var(--frame-darker) 100%);
    font-family: "Barlow", Arial, sans-serif;
  }
  .page {
    position: absolute; left: 194px; top: 0; width: 812px; height: 1200px;
    background: var(--page);
  }
  .question-mark {
    position: absolute; left: 266px; top: 68px; width: 132px; height: 256px;
  }
  .headline {
    position: absolute; left: 334px; top: 99px;
    font-weight: 700; font-size: 63px; line-height: 47px;
    letter-spacing: 0; text-transform: uppercase; color: var(--ink-grey);
  }
  .headline span { display: block; }
  .headline .accent { color: var(--accent-green); }
  .symptom-card {
    position: absolute; left: 158px; top: 399px; width: 495px; height: 650px;
    border: 2px solid var(--accent-green); border-radius: 8px;
  }
  .symptom-list {
    position: absolute; top: 37px; left: 0; right: 0; list-style: none;
    text-align: center; font-weight: 600; font-size: 42px; line-height: 47px;
    letter-spacing: 1px; text-transform: uppercase; color: var(--ink-grey);
  }
  .symptom-list .accent { color: var(--accent-green); }
  .divider {
    position: absolute; left: 207px; top: 250px; width: 79px; height: 5px;
    background: var(--faint-grey);
  }
  .divider::after {
    content: ""; position: absolute; left: 29px; top: 0; width: 22px; height: 5px;
    background: var(--accent-green);
  }
  .card-copy {
    position: absolute; left: 46px; top: 342px; width: 440px;
    font-size: 15.5px; line-height: 18.3px; color: var(--body-grey);
  }
  .card-copy p + p { margin-top: 18.5px; }
  .card-copy span { display: block; white-space: nowrap; }
  .next-block {
    position: absolute; left: 206px; top: 1126px; width: 400px; height: 74px;
    background: var(--soft-grey);
  }
</style>
</head>
<body>
  <main class="page">
    <svg class="question-mark" viewBox="0 0 132 256" aria-hidden="true">
      <path d="M8 70 A58 58 0 1 1 96 120 Q70 138 70 176 L70 196 L46 196 L46 170 Q46 128 80 104 A34 34 0 1 0 32 70 Z" fill="#f5f5f5"/>
      <rect x="54" y="222" width="32" height="34" fill="#f5f5f5"/>
    </svg>
    <h1 class="headline">
      <span>How it</span>
      <span>affect</span>
      <span>your</span>
      <span class="accent">health</span>
    </h1>
    <section class="symptom-card">
      <ul class="symptom-list">
        <li class="accent">Rash</li>
        <li>Watery eyes</li>
        <li class="accent">Coughing</li>
        <li>Itchy</li>
      </ul>
      <div class="divider"></div>
      <div class="card-copy">
        <p>
          <span>Amet orci eget eros faucibus tincidunt. Duis leo. Sed</span>
          <span>fringilla mauris sit amet nibh. Donec sodales sagittis</span>
          <span>magna. Sed consequat, leo eget bibendum sodales, augue</span>
          <span>velit cursus nunc, quis gravida magna mi a libero. Fusce</span>
          <span>vulputate eleifend sapien. Vestibulum purus quam,</span>
          <span>scelerisque ut, mollis sed, nonummy id, metus.</span>
        </p>
        <p>
          <span>Etiam ultricies nisi vel augue. Curabzitur ullamcorper</span>
          <span>ultricies nisi. Nam eget dui. Etiam rhoncus. Maecenas</span>
          <span>tempus, tellus eget condimentum rhoncus, sem quam</span>
          <span>semper libero, sit amet adipiscing sem neque sed ipsum.</span>
          <span>Nam quam nunc, blandit vel, luctus pulvinar, hendrerit id,</span>
          <span>lorem. Maecenas nec odio et ante tincidunt tempus. Donec</span>
          <span>vitae sapien ut libero venenatis faucibus. Nullam quis ante.</span>
        </p>
      </div>
    </section>
    <div class="next-block"></div>
  </main>
</body>
</html>
```